Business Card Design

Business Card for professional consulting firm working with large financial institutions.

Target Market(s)

Executive buyers

Industry/Entity Type

Banking

Contact Information for Business Card

Mild creativity wanted. Not boring, but do elaborate artwork.

Font styles to use
Serif
Sans Serif

Colors

Designer to choose colors to be used in the design.

Requirements
Must have
• Standard business card features - company name, individual name, telephone, website, email, locations.
Nice to have
• Two colors
Should not have
• too many colors, fancy printing, cartoons.

```html
<!DOCTYPE html>
<html lang="en">
<head>
<meta charset="utf-8">
<title>k7advisory — Business Card</title>
<link rel="stylesheet" href="https://fonts.googleapis.com/css2?family=Tinos:wght@400;700&display=swap">
<style>
  :root{
    --canvas:#e9e9e9;
    --paper:#ffffff;
    --ink:#111111;
    --muted:#7a7a7a;
    --silver:#c9c9c9;
    --night:#050505;
  }
  *{box-sizing:border-box;margin:0;padding:0}
  html,body{width:1200px;height:1200px;overflow:hidden}
  body{
    background:var(--canvas);
    font-family:"Tinos","Times New Roman",serif;
    display:flex;flex-direction:column;align-items:center;justify-content:center;gap:60px;
  }
  .card{
    position:relative;width:900px;height:514px;overflow:hidden;
    box-shadow:0 6px 18px rgba(0,0,0,.18);
  }
  /* front */
  .card--front{background:var(--paper);color:var(--ink)}
  .card__swoosh{position:absolute;inset:0;width:100%;height:100%}
  .brand{font-weight:400;letter-spacing:.5px}
  .card--front .brand{position:absolute;left:86px;top:58px;font-size:50px;color:var(--ink)}
  .person{position:absolute;left:40px;top:205px}
  .person__name{font-size:36px;font-weight:700;letter-spacing:.5px}
  .person__title{font-size:27px;color:var(--muted);margin-top:2px}
  .contacts{position:absolute;left:450px;top:195px;list-style:none}
  .contacts__rail{position:absolute;left:21px;top:20px;width:2px;height:156px;background:var(--silver)}
  .contact{position:relative;display:flex;align-items:center;height:40px;margin-bottom:12px;font-size:22px}
  .contact svg{width:42px;height:42px;margin-right:14px;flex:none}
  /* back */
  .card--back{background:var(--night);color:#fff}
  .card--back .brand{
    position:absolute;left:0;right:0;top:190px;text-align:center;font-size:58px;color:#f2f2f2;
  }
  .band{
    position:absolute;left:0;right:0;top:412px;height:44px;
    background:linear-gradient(90deg,#111 0%,#555 18%,#d8d8d8 45%,#eeeeee 55%,#8a8a8a 80%,#111 100%);
    display:flex;align-items:center;justify-content:center;
  }
  .band__url{font-size:24px;color:#1a1a1a}
</style>
</head>
<body>

<section class="card card--front" aria-label="Business card front">
  <svg class="card__swoosh" viewBox="0 0 900 514" preserveAspectRatio="none" aria-hidden="true">
    <path d="M0,375 C200,440 420,462 640,452 L900,420 L900,514 L0,514 Z" fill="#b9b9b9"/>
    <path d="M180,514 C380,470 650,440 900,418 L900,440 C650,462 420,490 340,514 Z" fill="#0a0a0a"/>
    <path d="M340,514 C420,490 650,462 900,440 L900,514 Z" fill="#ffffff"/>
  </svg>

  <div class="brand">k7advisory</div>

  <div class="person">
    <div class="person__name">JOHN DOE</div>
    <div class="person__title">Founder</div>
  </div>

  <ul class="contacts">
    <span class="contacts__rail"></span>
    <li class="contact">
      <svg viewBox="0 0 42 42"><polygon points="21,2 38,11.5 38,30.5 21,40 4,30.5 4,11.5" fill="#fff" stroke="#9a9a9a" stroke-width="2"/><path d="M21,12a6,6 0 0 1 6,6c0,5-6,11-6,11s-6-6-6-11a6,6 0 0 1 6-6z" fill="#222"/><circle cx="21" cy="18" r="2.2" fill="#fff"/></svg>
      Address
    </li>
    <li class="contact">
      <svg viewBox="0 0 42 42"><polygon points="21,2 38,11.5 38,30.5 21,40 4,30.5 4,11.5" fill="#fff" stroke="#9a9a9a" stroke-width="2"/><path d="M15,13l4-1 2,5-2.5,1.5c1,2.5 2.5,4 5,5l1.5-2.5 5,2-1,4c-8,1-15-6-14-14z" fill="#222"/></svg>
      123-546-7890
    </li>
    <li class="contact">
      <svg viewBox="0 0 42 42"><polygon points="21,2 38,11.5 38,30.5 21,40 4,30.5 4,11.5" fill="#fff" stroke="#9a9a9a" stroke-width="2"/><rect x="12" y="15" width="18" height="12" fill="#222"/><path d="M12,15l9,7 9-7" fill="none" stroke="#fff" stroke-width="1.5"/></svg>
      info@k7advisory.com
    </li>
    <li class="contact">
      <svg viewBox="0 0 42 42"><polygon points="21,2 38,11.5 38,30.5 21,40 4,30.5 4,11.5" fill="#fff" stroke="#9a9a9a" stroke-width="2"/><circle cx="21" cy="21" r="8" fill="#222"/><path d="M13,21h16M21,13c-4,5-4,11 0,16M21,13c4,5 4,11 0,16" fill="none" stroke="#fff" stroke-width="1.2"/></svg>
      www.k7advisory.com
    </li>
  </ul>
</section>

<section class="card card--back" aria-label="Business card back">
  <div class="brand">k7advisory</div>
  <div class="band"><span class="band__url">www.k7advisory.com</span></div>
</section>

</body>
</html>
```